TAVRELO GROUP OF CLINICS

We need a medical & lab report file. The design should be healthcare related. Our current file design has been used for almost 10 years. We need something more fresh & up-to-date. We have attached the current file design.

Need extra days to review

```html
<!DOCTYPE html>
<html lang="en">
<head>
<meta charset="utf-8">
<title>Tavrelo Group of Clinics – Medical Report File</title>
<link href="https://fonts.googleapis.com/css2?family=Poppins:wght@300;400;500;600;700&display=swap" rel="stylesheet">
<style>
:root{
  --navy:#2b2f8f;
  --blue:#1b8fd8;
  --sky:#27b5ee;
  --ink:#333842;
  --grey:#6b6f76;
  --paper:#ffffff;
  --tint:#f1f3f6;
  --stage:#d4d5d7;
}
*{margin:0;padding:0;box-sizing:border-box}
html,body{width:685px;height:1200px;overflow:hidden;background:var(--stage);font-family:"Poppins",sans-serif}
.spread-frame{position:absolute;left:20px;top:372px;width:645px;height:455px;box-shadow:0 6px 18px rgba(0,0,0,.18)}
.spread{position:absolute;left:0;top:0;width:1250px;height:880px;transform:scale(.516);transform-origin:0 0;background:linear-gradient(160deg,var(--paper) 0%,var(--tint) 100%);overflow:hidden}
.artwork{position:absolute;inset:0;width:1250px;height:880px}
.clinics-title{position:absolute;left:35px;top:40px;font-size:25px;font-weight:600;color:var(--navy);letter-spacing:.2px}
.clinics-title .accent{color:var(--sky)}
.clinic-card{position:absolute;width:277px;height:75px;border-radius:38px;background:var(--paper);border:3px solid #dfe2e6;border-left:7px solid var(--blue);box-shadow:0 3px 5px rgba(0,0,0,.12);padding:9px 12px 0 26px}
.clinic-name{font-size:11px;font-weight:600;color:var(--navy);display:flex;align-items:center;gap:4px;white-space:nowrap}
.pin{width:9px;height:11px;flex:none}
.clinic-detail{font-size:5.6px;line-height:7.4px;color:var(--ink);margin-top:3px;white-space:nowrap}
.clinic-detail b{font-weight:600}
.brand{position:absolute;display:flex;flex-direction:column;align-items:center;color:var(--navy);font-weight:600;text-align:center}
.brand .mark{border-radius:50%;background:var(--sky)}
.brand-main{left:663px;top:48px;width:160px;font-size:14px;gap:14px}
.brand-main .mark{width:100px;height:100px}
.brand-small{left:520px;top:812px;width:80px;font-size:7px;gap:5px}
.brand-small .mark{width:34px;height:34px}
.tagline{position:absolute;right:40px;top:44px;text-align:right;font-size:26px;font-weight:600;line-height:30px;color:var(--ink)}
.tagline .accent{color:var(--sky)}
.tagline .amp{font-weight:400}
.partner{position:absolute;right:38px;top:112px;font-size:13px;letter-spacing:4.3px;color:var(--ink)}
.report-title{position:absolute;right:40px;top:706px;text-align:right;line-height:50px}
.report-title .line-1{display:block;font-size:50px;font-weight:600;color:var(--navy)}
.report-title .line-2{display:block;font-size:50px;font-weight:300;color:var(--sky)}
.website{position:absolute;right:40px;top:820px;font-size:17px;letter-spacing:1.6px;color:var(--ink)}
.website b{font-weight:600;color:var(--navy)}
</style>
</head>
<body>
<div class="spread-frame">
  <div class="spread">
    <svg class="artwork" viewBox="0 0 1250 880">
      <defs>
        <linearGradient id="labTone" x1="0" y1="0.6" x2="1" y2="0.2">
          <stop offset="0" stop-color="#56677c"/>
          <stop offset=".25" stop-color="#3c72c4"/>
          <stop offset=".42" stop-color="#2f66d2"/>
          <stop offset=".6" stop-color="#8fb3dc"/>
          <stop offset=".78" stop-color="#dfe5ec"/>
          <stop offset="1" stop-color="#c9d2dc"/>
        </linearGradient>
      </defs>
      <polygon role="img" aria-label="Photo: lab technician in protective suit pipetting samples into blue test tube racks beside a microscope" points="0,668 1250,184 1250,522 255,880 0,880" fill="url(#labTone)"/>
      <line x1="0" y1="668" x2="1250" y2="184" stroke="var(--blue)" stroke-width="14"/>
      <line x1="0" y1="652" x2="1250" y2="168" stroke="var(--sky)" stroke-width="3"/>
    </svg>

    <h1 class="clinics-title">TAVRELO GROUP <span class="accent">OF CLINICS</span></h1>

    <svg width="0" height="0" style="position:absolute">
      <symbol id="pin-icon" viewBox="0 0 10 13"><path d="M5 0a4.5 4.5 0 0 0-4.5 4.5C.5 8 5 13 5 13s4.5-5 4.5-8.5A4.5 4.5 0 0 0 5 0zm0 6.3a1.8 1.8 0 1 1 0-3.6 1.8 1.8 0 0 1 0 3.6z" fill="#e5262d"/></symbol>
    </svg>

    <div class="clinic-card" style="left:28px;top:107px">
      <div class="clinic-name"><svg class="pin"><use href="#pin-icon"/></svg>PUSAT PERUBATAN TAVRELO</div>
      <p class="clinic-detail">Level 12, Wisma Cerah 4, Jalan Damai Baru, Off Jalan Seri Indah,<br>59100 Kuala Lumpur.</p>
      <p class="clinic-detail">Tel No: <b>+603-5510 2200</b> Fax No: +603-5510 2201<br>Email: tavrelo.central@mail.com</p>
    </div>
    <div class="clinic-card" style="left:318px;top:107px">
      <div class="clinic-name"><svg class="pin"><use href="#pin-icon"/></svg>KLINIK TAVRELO (BAYAN LEPAS)</div>
      <p class="clinic-detail">Lot 4B-1-2, 4B-1-3, Persiaran Cahaya, Seri Angsana, 11900 Bayan<br>Lepas, Penang.</p>
      <p class="clinic-detail">Tel No: <b>+604-380 1140</b> Fax No: +604-380 1141<br>Email: tavrelo.penang@mail.com</p>
    </div>
    <div class="clinic-card" style="left:28px;top:209px">
      <div class="clinic-name"><svg class="pin"><use href="#pin-icon"/></svg>KLINIK TAVRELO (BUKIT JELUTONG)</div>
      <p class="clinic-detail">No.22, Jalan Kenanga U8/D, Bukit Jelutong, 40150 Shah Alam, Selangor<br>Darul Ehsan.</p>
      <p class="clinic-detail">Tel No: <b>+603-7720 3310</b> Fax No: +603-7720 3311<br>Email: tavrelo.jelutong@mail.com</p>
    </div>
    <div class="clinic-card" style="left:318px;top:209px">
      <div class="clinic-name"><svg class="pin"><use href="#pin-icon"/></svg>KLINIK TAVRELO (SENDAYAN)</div>
      <p class="clinic-detail">No. 204, Jalan Niaga Sendayan 5/2, Pusat Niaga<br>Sendayan, 71950 Bandar Sri Sendayan, Negeri Sembilan.</p>
      <p class="clinic-detail">Tel No: <b>+606-640 2250</b> Fax No: +606-640 2251<br>Email: tavrelo.sendayan@mail.com</p>
    </div>
    <div class="clinic-card" style="left:28px;top:311px">
      <div class="clinic-name"><svg class="pin"><use href="#pin-icon"/></svg>TAVRELO MEDICAL CLINIC (KLIA2)</div>
      <p class="clinic-detail">S3-1.02, Landside Arrival Level, Terminal 2, 64000 Sepang, Selangor<br>Darul Ehsan.</p>
      <p class="clinic-detail">Tel No: <b>+603-8810 4400</b> Fax No: +603-8810 4401<br>Email: tavrelo.t2@mail.com</p>
    </div>
    <div class="clinic-card" style="left:318px;top:311px">
      <div class="clinic-name"><svg class="pin"><use href="#pin-icon"/></svg>TAVRELO MEDICAL CLINIC (KUA)</div>
      <p class="clinic-detail">Lot AR 07, Arrival Level, Main Terminal Building, 64000 Sepang,<br>Selangor Darul Ehsan.</p>
      <p class="clinic-detail">Tel No: <b>+603-8810 5500</b> Fax No: +603-8810 5501<br>Email: tavrelo.t1@mail.com</p>
    </div>
    <div class="clinic-card" style="left:28px;top:413px">
      <div class="clinic-name"><svg class="pin"><use href="#pin-icon"/></svg>TAVRELO MEDICAL CLINIC (PLA)</div>
      <p class="clinic-detail">Level 12, Wisma Cerah 4, Jalan Damai Baru, Off Jalan Seri Indah,<br>59100 Kuala Lumpur.</p>
      <p class="clinic-detail">Tel No: <b>+603-5510 2300</b> Fax No: +603-5510 2301<br>Email: tavrelo.pla@mail.com</p>
    </div>

    <div class="brand brand-main"><span class="mark"></span>TAVRELO GROUP</div>
    <div class="brand brand-small"><span class="mark"></span>TAVRELO GROUP</div>

    <p class="tagline"><span class="accent">PRIVATE</span> <span class="amp">&amp;</span><br>CONFIDENTIAL</p>
    <p class="partner">YOUR HEALTHCARE PARTNER</p>

    <h2 class="report-title"><span class="line-1">MEDICAL</span><span class="line-2">REPORT</span></h2>
    <p class="website">www.<b>tavrelogrp</b>.com</p>
  </div>
</div>
</body>
</html>
```